Optometrist/Eye Care Clinic Business card with new logo attached

We are a small, independent eye care clinic in Canada. We have recently updated our logo (as attached), and would like a professional, modern and health care oriented business card to highlight our office details and our optometrist. We'd like to incorporate the blue colours as seen on our logo.

Target Market(s)

demographic: age 35-65 male/female equal

Industry/Entity Type

Health Care

Contact Information for Business Card

Name of clinic: "Marrow Bend Eye Care Optometry"

Font styles to use
Sans Serif

Colors
0355a3

Requirements
Must have
• our website: marrowbendeyecare.com
• Dr Lena Quorvik
• Optometrist
• 217-392 E Halvering Ave
• Vancouver BC V6R 3J8
• P: 604-319-2058
• E: info@marrowbendeyecare.com
Nice to have
• front side: logo/name of clinic as seen on logo attached and website
• backside: logo on the left side, and name/title/address/phone/email

```html
<!DOCTYPE html>
<html lang="en">
<head>
<meta charset="utf-8">
<title>Marrow Bend Eye Care Optometry – Business Card</title>
<link href="https://fonts.googleapis.com/css2?family=Barlow:wght@600&family=Barlow+Semi+Condensed:wght@400;500&family=Questrial&display=swap" rel="stylesheet">
<style>
  :root {
    --backdrop: #dadddf;
    --paper: #ffffff;
    --ink-teal: #15607f;
    --brand-blue: #1e8db0;
    --brand-blue-deep: #19789a;
    --edge-navy: #0e4a6b;
    --band-light: #b6dceb;
    --url-teal: #2389ad;
    --text-light: #ffffff;
  }
  * { margin: 0; padding: 0; box-sizing: border-box; }
  html, body { width: 1000px; height: 1200px; overflow: hidden; }
  body { background: var(--backdrop); position: relative; }

  .card {
    position: absolute;
    left: 113px;
    width: 774px;
    height: 430px;
    background: var(--paper);
    box-shadow: 0 4px 14px rgba(0,0,0,0.18);
    overflow: hidden;
  }
  .card--front { top: 125px; }
  .card--back { top: 645px; }

  .brand-mark {
    position: absolute;
    border-radius: 50%;
    background: var(--ink-teal);
  }
  .brand-name {
    position: absolute;
    font-family: "Questrial", sans-serif;
    font-weight: 400;
    color: var(--ink-teal);
    text-align: center;
    line-height: 1;
    text-transform: uppercase;
  }
  .brand-name span { display: block; }

  /* front */
  .card--front .brand-mark { width: 150px; height: 150px; left: 312px; top: 48px; }
  .card--front .brand-name { left: 187px; width: 400px; top: 218px; }
  .card--front .brand-line-1 { font-size: 29px; letter-spacing: 4px; }
  .card--front .brand-line-2 { font-size: 46px; letter-spacing: 5px; margin-top: 8px; }
  .card--front .brand-line-3 { font-size: 20px; letter-spacing: 12px; margin-top: 8px; }
  .website {
    position: absolute;
    left: 0; width: 774px; top: 356px;
    text-align: center;
    font-family: "Questrial", sans-serif;
    font-size: 26px;
    letter-spacing: 8.5px;
    color: var(--url-teal);
  }

  /* back */
  .back-shapes { position: absolute; inset: 0; }
  .card--back .brand-mark { width: 130px; height: 130px; left: 90px; top: 72px; }
  .card--back .brand-name { left: 30px; width: 250px; top: 225px; }
  .card--back .brand-line-1 { font-size: 23px; letter-spacing: 3px; }
  .card--back .brand-line-2 { font-size: 36px; letter-spacing: 4px; margin-top: 6px; }
  .card--back .brand-line-3 { font-size: 16px; letter-spacing: 8px; margin-top: 6px; }

  .doctor {
    position: absolute;
    right: 67px; top: 74px;
    text-align: right;
    color: var(--text-light);
  }
  .doctor-name {
    font-family: "Barlow", sans-serif;
    font-weight: 600;
    font-size: 36px;
    letter-spacing: 1px;
    line-height: 1;
    text-transform: uppercase;
  }
  .doctor-name .title { font-size: 26px; margin-right: 4px; }
  .doctor-role {
    font-family: "Barlow Semi Condensed", sans-serif;
    font-weight: 500;
    font-size: 24px;
    letter-spacing: 3.5px;
    margin-top: 2px;
  }

  .contact-list {
    position: absolute;
    right: 22px; top: 190px;
    list-style: none;
    color: var(--text-light);
    font-family: "Barlow Semi Condensed", sans-serif;
    font-size: 20px;
    line-height: 23px;
  }
  .contact-item {
    display: flex;
    align-items: center;
    justify-content: flex-end;
    margin-bottom: 10px;
  }
  .contact-text { text-align: right; padding-right: 10px; border-right: 2px solid var(--text-light); }
  .contact-icon { width: 32px; display: flex; justify-content: center; margin-left: 6px; }
  .contact-icon svg { fill: var(--text-light); }
</style>
</head>
<body>

<section class="card card--front" aria-label="Business card front">
  <div class="brand-mark" aria-hidden="true"></div>
  <div class="brand-name">
    <span class="brand-line-1">Marrow Bend</span>
    <span class="brand-line-2">Eye Care</span>
    <span class="brand-line-3">Optometry</span>
  </div>
  <p class="website">marrowbendeyecare.com</p>
</section>

<section class="card card--back" aria-label="Business card back">
  <svg class="back-shapes" width="774" height="430" viewBox="0 0 774 430" aria-hidden="true">
    <path d="M251,0 C340,60 362,262 223,430 L774,430 L774,0 Z" fill="var(--band-light)"/>
    <path d="M282,0 C366,72 374,272 226,430 L774,430 L774,0 Z" fill="var(--edge-navy)"/>
    <path d="M294,0 C378,76 386,276 238,430 L774,430 L774,0 Z" fill="var(--brand-blue)"/>
    <circle cx="762" cy="-72" r="142" fill="var(--brand-blue-deep)"/>
    <ellipse cx="800" cy="520" rx="360" ry="175" fill="var(--brand-blue-deep)"/>
  </svg>

  <div class="brand-mark" aria-hidden="true"></div>
  <div class="brand-name">
    <span class="brand-line-1">Marrow Bend</span>
    <span class="brand-line-2">Eye Care</span>
    <span class="brand-line-3">Optometry</span>
  </div>

  <div class="doctor">
    <h1 class="doctor-name"><span class="title">Dr</span>Lena Quorvik</h1>
    <p class="doctor-role">optometrist</p>
  </div>

  <ul class="contact-list">
    <li class="contact-item">
      <span class="contact-text">217-392 E Halvering Ave<br>Vancouver BC V6R 3J8</span>
      <span class="contact-icon">
        <svg width="18" height="28" viewBox="0 0 18 28" aria-label="Address"><path d="M9 0C4 0 0 4 0 9c0 7 9 19 9 19s9-12 9-19c0-5-4-9-9-9zm0 13a4 4 0 1 1 0-8 4 4 0 0 1 0 8z"/></svg>
      </span>
    </li>
    <li class="contact-item">
      <span class="contact-text">604-319-2058</span>
      <span class="contact-icon">
        <svg width="22" height="24" viewBox="0 0 24 24" aria-label="Phone"><path d="M6.6 10.8c1.4 2.8 3.8 5.1 6.6 6.6l2.2-2.2c.3-.3.7-.4 1-.2 1.1.4 2.3.6 3.6.6.6 0 1 .4 1 1V20c0 .6-.4 1-1 1C10.6 21 3 13.4 3 4c0-.6.4-1 1-1h3.5c.6 0 1 .4 1 1 0 1.3.2 2.5.6 3.6.1.3 0 .7-.2 1L6.6 10.8z"/></svg>
      </span>
    </li>
    <li class="contact-item">
      <span class="contact-text">info@marrowbendeyecare.com</span>
      <span class="contact-icon">
        <svg width="30" height="20" viewBox="0 0 30 20" aria-label="Email"><path d="M0 0h30v20H0z M2 2v1l13 9 13-9V2z" fill-rule="evenodd"/></svg>
      </span>
    </li>
  </ul>
</section>

</body>
</html>
```